Amber Heron Fund Pitch Deck

This is a PowerPoint for use in investor presentations. The copy is written (although it may have small tweaks) and the designer will be responsible for creating a template and some graphical representations inside the presentation.

Note on the logo. Only the Amber Heron should be used, not the text.

```html
<!DOCTYPE html>
<html lang="en">
<head>
<meta charset="utf-8">
<title>Amber Heron Fund Pitch Deck</title>
<link rel="stylesheet" href="https://fonts.googleapis.com/css2?family=Inter:wght@400;600;800&display=swap">
<style>
:root{
  --blue:#5473c4;
  --blue-dark:#3a58a8;
  --ink:#151515;
  --text:#555a63;
  --canvas:#ececef;
  --slide:#ffffff;
  --ring:#c9ccd2;
  --photo-a:#8d8f96;
  --photo-b:#c9c4bd;
}
*{box-sizing:border-box;margin:0;padding:0}
html,body{width:1200px;height:4048px;overflow:hidden}
body{background:var(--canvas);font-family:"Inter",Arial,sans-serif;color:var(--ink);padding-top:80px}
.slide{position:relative;width:1056px;height:594px;margin:0 auto 66px;background:var(--slide);overflow:hidden;box-shadow:0 2px 10px rgba(0,0,0,.08)}
.slide svg.art{position:absolute;inset:0;width:100%;height:100%}
.brand{position:absolute;display:flex;align-items:center;gap:8px;font-weight:800;font-size:19px;color:var(--blue);letter-spacing:.2px}
.brand .dot{width:14px;height:14px;border-radius:50%;background:var(--blue)}
.title{position:absolute;font-weight:800;font-size:50px;line-height:1.05;color:var(--ink)}
.copy{position:absolute;font-size:13.5px;line-height:1.6;color:var(--text)}
.copy p+p{margin-top:14px}
.bullets{list-style:none;margin-top:18px}
.bullets li{display:flex;align-items:center;gap:12px;font-weight:600;color:var(--ink);font-size:15px;margin-top:10px}
.bullets li::before{content:"";width:14px;height:14px;border-radius:50%;background:var(--blue);box-shadow:0 0 0 3px #d8e0f3}
.step{position:absolute;width:150px;text-align:center;font-size:12.5px;line-height:1.45;color:var(--text)}
.step-note{position:absolute;left:80px;right:80px;bottom:44px;text-align:center;font-weight:600;font-size:15px;line-height:1.5;color:var(--ink)}
</style>
</head>
<body>

<!-- Slide 1: The Edge -->
<section class="slide edge">
  <svg class="art" viewBox="0 0 1056 594">
    <defs><linearGradient id="ph1" x1="0" y1="0" x2="1" y2="1"><stop offset="0" stop-color="#d9d6d1"/><stop offset="1" stop-color="#6f7480"/></linearGradient></defs>
    <path d="M560 0 A470 470 0 0 0 600 594" fill="none" stroke="var(--blue)" stroke-width="9"/>
    <path role="img" aria-label="Photo of business team reviewing documents" d="M600 0 H1056 V594 H640 A470 470 0 0 1 600 0 Z" fill="url(#ph1)"/>
    <circle cx="600" cy="470" r="88" fill="#fff" stroke="var(--ring)" stroke-width="10"/>
    <circle role="img" aria-label="Photo of colleagues in discussion" cx="600" cy="470" r="76" fill="url(#ph1)"/>
  </svg>
  <div class="brand" style="left:64px;top:34px"><span class="dot"></span>Amber Heron</div>
  <h1 class="title" style="left:64px;top:160px">The Edge</h1>
  <div class="copy" style="left:64px;top:240px;width:420px">
    <p>Experience with fund management and asset disposal. Utilizing the credit trail from both borrowers and guarantors taken on the Internet, we can operate special service assets and collect on them more quickly and thoroughly than most.</p>
    <p>Much of the technology and experience as a team can be attributed to the lead's experience at Fieldstone. The principals were the management team that came on in March 2020 and grew the business from less than 10,000 PPP loans to more than 400,000.</p>
  </div>
</section>

<!-- Slide 2: The Technology -->
<section class="slide technology">
  <svg class="art" viewBox="0 0 1056 594">
    <defs><linearGradient id="ph2" x1="0" y1="0" x2="1" y2="1"><stop offset="0" stop-color="#4c4a4c"/><stop offset=".6" stop-color="#a07a55"/><stop offset="1" stop-color="#d9c8b2"/></linearGradient></defs>
    <rect x="0" y="150" width="110" height="400" fill="var(--blue)"/>
    <rect role="img" aria-label="Photo of business meeting around a table" x="60" y="44" width="470" height="480" rx="36" fill="url(#ph2)"/>
  </svg>
  <div class="brand" style="right:56px;top:34px"><span class="dot"></span>Amber Heron</div>
  <h1 class="title" style="left:600px;top:150px;font-size:44px">The Technology</h1>
  <div class="copy" style="left:600px;top:220px;width:400px">
    <p>Most lenders and servicers use credit bureau scores and their software like RecordLink for collections.</p>
    <p>These software packages fail to address the most important factors which is to analyze the borrower (and the guarantors) to allow for customized collection plans. We use enhanced data tracking developed during PPP forgiveness and collection efforts with advanced social media tags.</p>
    <p>Finally, we use evolving algorithms to price and purchase NPL portfolios at the correct price.</p>
  </div>
</section>

<!-- Slide 3: The Market -->
<section class="slide market">
  <svg class="art" viewBox="0 0 1056 594">
    <defs><linearGradient id="ph3" x1="0" y1="0" x2="1" y2="1"><stop offset="0" stop-color="#2b2f3a"/><stop offset=".5" stop-color="#6d6f78"/><stop offset="1" stop-color="#cfd2d8"/></linearGradient></defs>
    <rect x="830" y="0" width="226" height="594" fill="var(--blue)"/>
    <rect role="img" aria-label="Photo of business handshake" x="520" y="70" width="460" height="460" rx="36" fill="url(#ph3)"/>
  </svg>
  <div class="brand" style="left:64px;top:34px"><span class="dot"></span>Amber Heron</div>
  <h1 class="title" style="left:64px;top:270px">The Market</h1>
  <div class="copy" style="left:64px;top:345px;width:400px">
    <p>The commercial lending market size was valued at $8,803.03 billion in 2020, and is projected to reach $24,275.95 billion by 2030, growing at a CAGR of 10.7% from 2021 to 2030.</p>
    <p>The credit cycle is entering into a period of rising interest rates and corresponding defaults. The fund seeks to take advantage of that emerging opportunity.</p>
  </div>
</section>

<!-- Slide 4: Our Process -->
<section class="slide process">
  <svg class="art" viewBox="0 0 1056 594">
    <defs><linearGradient id="ph4" x1="0" y1="0" x2="0" y2="1"><stop offset="0" stop-color="#fff"/><stop offset=".5" stop-color="#e8eaee"/><stop offset="1" stop-color="#fff"/></linearGradient></defs>
    <rect role="img" aria-label="Faint background photo of an office" x="0" y="120" width="1056" height="330" fill="url(#ph4)"/>
    <line x1="40" y1="300" x2="1016" y2="300" stroke="var(--blue)" stroke-width="3"/>
    <g fill="none" stroke="var(--blue)" stroke-width="1.5">
      <line x1="150" y1="230" x2="150" y2="274"/><line x1="283" y1="326" x2="283" y2="360"/>
      <line x1="416" y1="230" x2="416" y2="274"/><line x1="549" y1="326" x2="549" y2="360"/>
      <line x1="682" y1="230" x2="682" y2="274"/><line x1="815" y1="326" x2="815" y2="360"/>
      <line x1="948" y1="230" x2="948" y2="274"/>
    </g>
    <g fill="#fff" stroke="var(--blue)" stroke-width="3">
      <circle cx="150" cy="300" r="24"/><circle cx="283" cy="300" r="24"/><circle cx="416" cy="300" r="24"/>
      <circle cx="549" cy="300" r="24"/><circle cx="682" cy="300" r="24"/><circle cx="815" cy="300" r="24"/><circle cx="948" cy="300" r="24"/>
    </g>
    <g fill="var(--blue)">
      <circle cx="150" cy="300" r="6"/><circle cx="283" cy="300" r="6"/><circle cx="416" cy="300" r="6"/>
      <circle cx="549" cy="300" r="6"/><circle cx="682" cy="300" r="6"/><circle cx="815" cy="300" r="6"/><circle cx="948" cy="300" r="6"/>
    </g>
  </svg>
  <h1 class="title" style="left:56px;top:36px;font-size:40px">Our Process</h1>
  <div class="brand" style="right:56px;top:40px"><span class="dot"></span>Amber Heron</div>
  <p class="step" style="left:75px;top:170px">Work with our lender customers on their non-performing loan portfolio.</p>
  <p class="step" style="left:208px;top:368px">Purchase participation in non-performing loans.</p>
  <p class="step" style="left:341px;top:170px">Provide special servicing in compliance with bank's servicing criteria.</p>
  <p class="step" style="left:474px;top:368px">Provide fresh access to NPL platform.</p>
  <p class="step" style="left:607px;top:170px">Maintain first right of refusal to purchase loan using proprietary algorithm.</p>
  <p class="step" style="left:740px;top:368px">Internal servicing standards.</p>
  <p class="step" style="left:873px;top:188px">Liquidations when necessary.</p>
  <p class="step-note">Initially partner with licensed collection agencies to supplement our in-house abilities (and comply with regulatory requirements). Potential to acquire and bring completely in-house</p>
</section>

<!-- Slide 5: Our Customers -->
<section class="slide customers">
  <svg class="art" viewBox="0 0 1056 594">
    <defs><linearGradient id="ph5" x1="0" y1="0" x2="1" y2="1"><stop offset="0" stop-color="#c8a27a"/><stop offset=".6" stop-color="#7b6a5e"/><stop offset="1" stop-color="#3f4048"/></linearGradient></defs>
    <path d="M400 0 A470 470 0 0 1 420 594" fill="none" stroke="var(--blue)" stroke-width="9"/>
    <path role="img" aria-label="Photo of a man working on a laptop" d="M0 0 H360 A470 470 0 0 1 380 594 H0 Z" fill="url(#ph5)"/>
    <circle cx="400" cy="470" r="88" fill="#fff" stroke="var(--ring)" stroke-width="10"/>
    <circle role="img" aria-label="Photo of colleagues at a desk" cx="400" cy="470" r="76" fill="url(#ph5)"/>
  </svg>
  <div class="brand" style="right:56px;top:34px"><span class="dot"></span>Amber Heron</div>
  <h1 class="title" style="left:560px;top:170px;font-size:44px">Our Customers</h1>
  <div class="copy" style="left:560px;top:240px;width:420px">
    <p>Target Market: It would seem we should narrow the target market and also point out any special relationships, people that likely can source from their experience or otherwise explain why we have a leg up on pipeline.</p>
    <ul class="bullets">
      <li>Community banks: Nearly 5,000</li>
      <li>Mid-Market banks: Approximately 4,000</li>
    </ul>
  </div>
</section>

<!-- Slide 6: Advantage -->
<section class="slide advantage">
  <svg class="art" viewBox="0 0 1056 594">
    <defs><linearGradient id="ph6" x1="0" y1="0" x2="1" y2="1"><stop offset="0" stop-color="#e4e6ea"/><stop offset=".5" stop-color="#7c8089"/><stop offset="1" stop-color="#2d3038"/></linearGradient></defs>
    <rect x="530" y="0" width="14" height="594" fill="var(--blue)"/>
    <rect role="img" aria-label="Photo of business partners shaking hands in an office" x="544" y="0" width="512" height="594" fill="url(#ph6)"/>
  </svg>
  <div class="brand" style="left:64px;top:34px"><span class="dot"></span>Amber Heron</div>
  <h1 class="title" style="left:64px;top:270px;font-size:44px">Advantage</h1>
  <div class="copy" style="left:64px;top:335px;width:400px">
    <p>Tech + Capital (yes, emphasize high tech approach to understanding credit performance, verification of circumstances etc.. this may be the most important slide.. Capital as a percentage of total and significant co-investment against first round of raise.</p>
  </div>
</section>

</body>
</html>
```